Need Business Card ASAP

We need a business card design for a meeting coming up in a few days. The company name is Halvorne Building and Construction and the logo is attached. Something clean, cool, and contemporary that we can get to a printer right away. Attached is the business card for Murrow Energy, an affiliated company, which we like. Instead of the hawk on the back, you could use the attached "D". We'll also be needing matching letterhead in the near future, so ideas for that are welcome.

```html
<!DOCTYPE html>
<html lang="en">
<head>
<meta charset="utf-8">
<title>Halvorne Building and Construction – Business Card</title>
<link rel="stylesheet" href="https://fonts.googleapis.com/css2?family=Arimo:wght@400;700&display=swap">
<style>
  :root {
    --backdrop: #e9e6df;
    --card-white: #ffffff;
    --card-dark: #3a3a3a;
    --gold: #cdc6a2;
    --gold-text: #b8ae80;
    --ink: #1e1e1e;
    --grey-text: #555555;
    --divider: #b9b9b9;
  }
  * { margin: 0; padding: 0; box-sizing: border-box; }
  html, body {
    width: 1034px; height: 1200px; overflow: hidden;
    background: var(--backdrop);
    font-family: "Arimo", Arial, sans-serif;
  }
  .canvas { position: relative; width: 1034px; height: 1200px; }

  /* Front of card */
  .card-front {
    position: absolute; left: 79px; top: 59px; width: 888px; height: 504px;
    background: var(--card-white); border-radius: 25px; overflow: hidden;
    box-shadow: 0 4px 14px rgba(0,0,0,.18);
  }
  .brand-block { position: absolute; left: 109px; top: 39px; width: 268px; }
  .brand-square { width: 268px; height: 210px; background: var(--gold); }
  .brand-name {
    margin-top: 30px; text-align: center;
    font-size: 46px; font-weight: 400; color: var(--ink);
  }
  .divider {
    position: absolute; left: 416px; top: 42px; width: 3px; height: 342px;
    background: linear-gradient(to bottom, transparent, var(--divider) 25%, var(--divider) 75%, transparent);
  }
  .contact { position: absolute; left: 457px; top: 30px; }
  .person-name { font-size: 34px; font-weight: 700; color: var(--gold-text); line-height: 1.1; }
  .person-title { font-size: 22px; font-weight: 700; color: var(--ink); margin-top: 6px; }
  .company-name {
    font-size: 28px; font-weight: 700; color: var(--gold-text);
    line-height: 34px; margin-top: 22px;
  }
  .address { font-size: 21px; color: var(--grey-text); line-height: 31px; margin-top: 8px; }
  .lines { list-style: none; margin-top: 16px; }
  .lines li {
    display: flex; align-items: center; gap: 10px;
    font-size: 25px; color: var(--ink); height: 41px;
  }
  .lines svg { width: 16px; height: 16px; flex: none; }
  .bands { position: absolute; left: 0; top: 0; }
  .web-front {
    position: absolute; right: 118px; top: 446px;
    font-size: 25px; letter-spacing: 1.5px; color: var(--ink);
  }

  /* Back of card */
  .card-back {
    position: absolute; left: 61px; top: 625px; width: 931px; height: 504px;
    background: var(--card-dark); border-radius: 37px;
    box-shadow: 0 4px 14px rgba(0,0,0,.25);
  }
  .back-name {
    position: absolute; left: 0; right: 0; top: 190px; text-align: center;
    font-size: 96px; font-weight: 700; color: var(--card-white);
  }
  .web-back {
    position: absolute; left: 0; right: 0; top: 442px; text-align: center;
    font-size: 27px; font-weight: 700; letter-spacing: 1.5px; color: var(--card-white);
  }
</style>
</head>
<body>
<div class="canvas">

  <section class="card-front">
    <div class="brand-block">
      <div class="brand-square"></div>
      <div class="brand-name">Halvorne</div>
    </div>

    <div class="divider"></div>

    <div class="contact">
      <div class="person-name">Your Name</div>
      <div class="person-title">Title</div>
      <div class="company-name">Halvorne Building<br>&amp; Construction</div>
      <div class="address">00, Complex Name, Street<br>City 00000</div>
      <ul class="lines">
        <li>
          <svg viewBox="0 0 16 16" aria-hidden="true"><circle cx="8" cy="8" r="7" fill="none" stroke="#b8ae80" stroke-width="1.5"/><path d="M5.5 4.5c0 4 2 6 6 6" fill="none" stroke="#b8ae80" stroke-width="2" stroke-linecap="round"/></svg>
          (123) 456-7890
        </li>
        <li>
          <svg viewBox="0 0 16 16" aria-hidden="true"><rect x="4" y="1" width="8" height="14" rx="1.5" fill="none" stroke="#b8ae80" stroke-width="1.5"/><rect x="6" y="3.5" width="4" height="5" fill="#b8ae80"/></svg>
          (123) 456-7890
        </li>
        <li>
          <svg viewBox="0 0 16 16" aria-hidden="true"><rect x="1" y="3.5" width="14" height="9" rx="1" fill="#b8ae80"/><path d="M1.5 4l6.5 5 6.5-5" fill="none" stroke="#fff" stroke-width="1.2"/></svg>
          yourname@halvorne.com
        </li>
      </ul>
    </div>

    <svg class="bands" width="888" height="504" viewBox="0 0 888 504" aria-hidden="true">
      <polygon points="0,463 380,463 375,471 0,471" fill="#cdc6a2"/>
      <polygon points="0,435 398,435 383,457 0,457" fill="#1e1e1e"/>
      <polygon points="411,429 888,429 888,504 362,504" fill="#cdc6a2"/>
    </svg>
    <div class="web-front">www.halvorne.com</div>
  </section>

  <section class="card-back">
    <div class="back-name">Halvorne</div>
    <div class="web-back">www.halvornebuilding.com</div>
  </section>

</div>
</body>
</html>
```